New flyer design for construction company marketing and description of services.

I want to have a flyer design that my techs will carry to deliver after job completion or for marketing purposes, to explain what services we provide, we offer General construction services.

Brightnail Handyman Sevices originated from a family-owned and operated contractor business, performing home renovation, addition, and construction work in the NYC area since 2004.

Today, we specialize in reliable and affordable Construction services for residential and commercial clients In 2014, we expanded to northern New Jersey. In 2016, we brought quality home improvement and repair services to new Bucks County, PA, and nearby New Jersey areas.
We offer carpentry, electrical, plumbing, renovation, remodel, cleaning services and landscaping.
I would like to have a section for home rental maintenance.

Target Market(s)

Homeowners, rental properties, real state and Senior citizen

Industry/Entity Type

Construction Company

Colors

Designer to choose colors to be used in the design.

Requirements
Must have
• A special design that will attract 55 + clients maybe a logo version that will be more attractive to seniors. I would updated the briefing with design and previous pictures, but we have all available in our social media instagram and facebook:
• https://www.sampleinsta.test/brightnailhandyman/?hl=en
• https://www.samplefacebook.test/brightnailhandy/
Nice to have
• New design ideas and layouts.

```html
<!DOCTYPE html>
<html lang="en">
<head>
<meta charset="utf-8">
<title>Brightnail Handyman Sevices – Flyer</title>
<link href="https://fonts.googleapis.com/css2?family=Bebas+Neue&family=Roboto:wght@400;700&family=Oswald:wght@500;600&display=swap" rel="stylesheet">
<style>
:root{
  --red:#e30613;
  --black:#111111;
  --dark:#1c1c1c;
  --white:#ffffff;
  --light:#ececec;
  --grey:#555555;
  --icon:#6b6b6b;
}
*{margin:0;padding:0;box-sizing:border-box}
html,body{width:771px;height:1200px;overflow:hidden;background:var(--white)}
body{position:relative;font-family:"Roboto",Arial,sans-serif}
.panel{position:absolute;left:45px;width:794px;overflow:hidden;transform-origin:0 0;transform:scale(.8577)}
.front{top:75px;height:559px;background:var(--black)}
.back{top:638px;height:561px;background:var(--light)}
.abs{position:absolute;z-index:2}
.art{position:absolute;inset:0;z-index:1}
.heading{font-family:"Oswald",sans-serif;font-weight:600;color:var(--white);font-size:17px;letter-spacing:.3px}
.heading::after{content:"";display:block;width:46px;height:3px;background:var(--red);margin-top:3px}
.body-copy{font-size:9.4px;line-height:12.6px;color:#e6e6e6;text-align:justify}
.body-copy+.body-copy{margin-top:9px}
.contact{list-style:none;color:var(--white);font-size:9.6px}
.contact li{display:flex;align-items:center;gap:6px;height:16.5px;white-space:nowrap}
.contact li.phone{font-weight:700;font-size:13px;height:20px}
.contact li.long{font-size:9px}
.contact svg{width:9px;height:9px;flex:none}
.social{display:flex;gap:2px;margin-top:5px}
.social span{width:11px;height:11px;border:1px solid var(--white);border-radius:50%}
.brand{display:flex;align-items:center;gap:7px;color:var(--white);font-family:"Roboto",sans-serif;font-weight:700;white-space:nowrap}
.brand .dot{border-radius:50%;background:var(--red);flex:none}
.tagline{font-family:"Bebas Neue",sans-serif;color:var(--white);line-height:.95}
.tagline .small{font-size:36px;display:block}
.tagline .big{font-size:52px;display:block}
.vertical-url{position:absolute;z-index:2;left:776px;bottom:8px;transform-origin:0 100%;transform:rotate(-90deg);color:var(--white);font-size:15px;white-space:nowrap;font-family:"Roboto",sans-serif}
/* back */
.photo-band{position:absolute;left:0;top:0;width:397px;height:211px;background:linear-gradient(180deg,#8fa3b5 0%,#c9ccd0 45%,#7d7f80 100%)}
.about-box{position:absolute;left:0;top:118px;width:397px;height:93px;background:rgba(20,20,20,.82);padding:6px 28px 0 28px}
.about-box .title{font-family:"Bebas Neue",sans-serif;color:var(--white);font-size:19px;line-height:19px}
.about-box p{font-size:8.3px;line-height:10.8px;color:#e2e2e2;text-align:justify;margin-top:3px}
.offer-title{position:absolute;left:28px;top:216px;font-family:"Bebas Neue",sans-serif;font-size:19px;color:var(--black)}
.offer-title::after{content:"";display:block;width:30px;height:2px;background:var(--red)}
.service-label{position:absolute;height:15px;display:flex;align-items:center}
.service-label b{background:var(--red);color:var(--white);font-size:9.5px;font-weight:700;height:15px;line-height:15px;padding-left:27px;letter-spacing:.3px}
.service-label i{width:17px;height:15px;background:repeating-linear-gradient(110deg,var(--black) 0 3px,transparent 3px 6px);margin-left:2px}
.right .service-label b{padding-left:20px}
.service-copy{position:absolute;font-size:8.5px;line-height:11.6px;color:var(--grey);text-align:justify}
.divider{position:absolute;height:1px;background:#cfcfcf}
.hex-icon{position:absolute;width:82px;height:90px}
.rental{position:absolute;left:397px;top:413px;width:397px;height:148px;background:var(--dark);padding:10px 20px 0 20px}
.rental h3{color:var(--white);font-size:11px;font-weight:700;letter-spacing:.2px;margin-bottom:8px}
.rental ul{list-style:none}
.rental li{display:flex;gap:7px;color:#e0e0e0;font-size:7.8px;line-height:10.4px;margin-bottom:8px}
.rental li svg{width:8px;height:8px;flex:none;margin-top:1px}
</style>
</head>
<body>

<!-- FRONT SPREAD -->
<section class="panel front">
  <svg class="art" viewBox="0 0 794 559" width="794" height="559">
    <defs>
      <linearGradient id="diner" x1="0" y1="0" x2="0" y2="1"><stop offset="0" stop-color="#8e8a84"/><stop offset="1" stop-color="#e6e4e0"/></linearGradient>
      <linearGradient id="bedroom" x1="0" y1="0" x2="0" y2="1"><stop offset="0" stop-color="#7f98a8"/><stop offset=".6" stop-color="#c9ccce"/><stop offset="1" stop-color="#8a6a45"/></linearGradient>
      <linearGradient id="sauna" x1="0" y1="0" x2="1" y2="0"><stop offset="0" stop-color="#6b3520"/><stop offset=".5" stop-color="#b88a55"/><stop offset="1" stop-color="#5b3424"/></linearGradient>
      <linearGradient id="kitchen" x1="0" y1="0" x2="0" y2="1"><stop offset="0" stop-color="#d6d2c8"/><stop offset="1" stop-color="#7a6450"/></linearGradient>
    </defs>
    <polygon fill="var(--red)" points="557,0 660,0 640,16"/>
    <polygon fill="var(--red)" points="397,559 397,440 485,395 602,460 719,395 719,200 794,200 794,559"/>
    <polygon role="img" aria-label="Photo of a finished restaurant interior" fill="url(#diner)" stroke="#fff" stroke-width="9" points="702,-13 810,50 810,175 702,237 594,175 594,50"/>
    <polygon role="img" aria-label="Photo of a renovated bedroom" fill="url(#bedroom)" stroke="#fff" stroke-width="9" points="355,165 474,234 474,371 355,439 236,371 236,234"/>
    <polygon role="img" aria-label="Photo of a wooden sauna door" fill="url(#sauna)" stroke="#fff" stroke-width="9" points="602,167 719,235 719,370 602,437 485,370 485,235"/>
    <polygon role="img" aria-label="Photo of a finished kitchen corner" fill="url(#kitchen)" stroke="#fff" stroke-width="9" points="232,392 345,457 345,587 232,652 119,587 119,457"/>
  </svg>

  <div class="abs" style="left:24px;top:40px;width:336px">
    <h2 class="heading">ABOUT US</h2>
    <p class="body-copy" style="margin-top:9px">We began as a family-owned contractor business, doing home renovation, additions and construction work across the NYC area since 2004. Our crews treat every home with care and finish each job cleanly.</p>
    <p class="body-copy">Today we offer reliable, affordable services for homeowners, rental owners and seniors in New York, northern New Jersey and Bucks County, with honest prices and friendly techs.</p>
  </div>

  <div class="abs" style="left:21px;top:238px;width:205px">
    <h2 class="heading" style="font-size:12.5px">GET IN TOUCH</h2>
    <ul class="contact" style="margin-top:8px">
      <li class="phone"><svg viewBox="0 0 10 10"><path d="M2 1l2 2-1 1.2c.6 1.2 1.5 2.1 2.8 2.8L7 6l2 2-1.3 1.3C4.5 9 1 5.5.7 2.3z" fill="none" stroke="#fff" stroke-width=".9"/></svg>555 010 3415</li>
      <li class="long"><svg viewBox="0 0 10 10"><rect x="1" y="1" width="8" height="8" rx="2" fill="none" stroke="#fff"/><circle cx="5" cy="5" r="1.8" fill="none" stroke="#fff"/></svg>www.sampleinsta.test/brightnailhandyman</li>
      <li><svg viewBox="0 0 10 10"><rect x=".5" y="2" width="9" height="6" fill="none" stroke="#fff"/><path d="M.5 2L5 5.5 9.5 2" fill="none" stroke="#fff"/></svg>brightnailhandymannyc@mail.test</li>
      <li><svg viewBox="0 0 10 10"><circle cx="5" cy="5" r="4" fill="none" stroke="#fff"/><path d="M1 5h8M5 1c-2 2.5-2 5.5 0 8M5 1c2 2.5 2 5.5 0 8" fill="none" stroke="#fff" stroke-width=".7"/></svg>www.brightnail.test</li>
    </ul>
    <div class="social"><span></span><span></span><span></span><span></span><span></span></div>
  </div>

  <div class="brand abs" style="left:18px;top:380px;font-size:24px"><span class="dot" style="width:24px;height:24px"></span>brightnail</div>

  <div class="brand abs" style="left:414px;top:86px;font-size:25px"><span class="dot" style="width:28px;height:28px"></span>brightnail</div>

  <div class="tagline abs" style="left:420px;top:466px">
    <span class="small">A BETTER WAY TO</span>
    <span class="big">GET TASKS DONE</span>
  </div>

  <div class="vertical-url">www.brightnailh.test</div>
</section>

<!-- BACK SPREAD -->
<section class="panel back">
  <div class="photo-band" role="img" aria-label="Photo of a house patio with a white pergola"></div>
  <div class="about-box">
    <h2 class="title">ABOUT US</h2>
    <p>Brightnail Handyman Sevices grew from a family contractor business working in NYC since 2004. In 2014 we expanded to northern New Jersey, and in 2016 we brought quality home improvement and repair to Bucks County, PA. Residential and commercial clients trust us for careful, on-time work.</p>
  </div>

  <h2 class="offer-title">WE OFFER</h2>

  <!-- left column services -->
  <div class="service-label" style="left:0;top:246px"><b style="width:110px">CARPENTRY</b><i></i></div>
  <p class="service-copy" style="left:28px;top:268px;width:250px">Custom shelves, trim, doors, decks and framing built to last. We repair rot, squeaks and loose boards, and fit new cabinets so every room feels solid and looks finished from floor to ceiling.</p>
  <svg class="hex-icon" style="left:299px;top:231px" viewBox="0 0 82 90"><polygon points="41,4 77,24 77,66 41,86 5,66 5,24" fill="#fff" stroke="var(--red)" stroke-width="5"/><rect x="24" y="40" width="34" height="22" rx="2" fill="var(--icon)"/><path d="M34 40v-5h14v5" fill="none" stroke="var(--icon)" stroke-width="3"/><rect x="28" y="27" width="4" height="14" fill="var(--icon)" transform="rotate(-25 30 34)"/></svg>
  <div class="divider" style="left:0;top:343px;width:397px"></div>

  <div class="service-label" style="left:0;top:348px"><b style="width:110px">ELECTRICAL</b><i></i></div>
  <p class="service-copy" style="left:28px;top:372px;width:250px">Safe, code-compliant wiring, outlets, switches and light fixtures. We install ceiling fans, smoke detectors and panel upgrades, and track down flickers or tripping breakers quickly.</p>
  <svg class="hex-icon" style="left:301px;top:346px" viewBox="0 0 82 90"><polygon points="41,4 77,24 77,66 41,86 5,66 5,24" fill="#fff" stroke="var(--red)" stroke-width="5"/><circle cx="41" cy="42" r="10" fill="var(--icon)"/><rect x="36" y="52" width="10" height="8" fill="var(--icon)"/><path d="M41 24v5M26 42h-5M61 42h-5M30 31l-3-3M52 31l3-3" stroke="var(--icon)" stroke-width="2.5"/></svg>
  <div class="divider" style="left:0;top:446px;width:397px"></div>

  <div class="service-label" style="left:0;top:462px"><b style="width:110px">PLUMBING</b><i></i></div>
  <p class="service-copy" style="left:32px;top:486px;width:246px">Leaky faucets, running toilets, clogged drains and new fixtures handled with care. We replace sinks, shut-off valves and water heaters and leave your kitchen and bath clean.</p>
  <svg class="hex-icon" style="left:301px;top:459px" viewBox="0 0 82 90"><polygon points="41,4 77,24 77,66 41,86 5,66 5,24" fill="#fff" stroke="var(--red)" stroke-width="5"/><rect x="20" y="36" width="34" height="9" fill="var(--icon)"/><rect x="36" y="27" width="8" height="9" fill="var(--icon)"/><path d="M54 36h6v18h-8" fill="var(--icon)"/><path d="M58 58c-2 4 4 4 2 0l-1-3z" fill="var(--icon)"/></svg>

  <!-- right column services -->
  <div class="right">
    <div class="service-label" style="left:397px;top:13px"><b style="width:126px">RENOVATION</b><i></i></div>
    <p class="service-copy" style="left:418px;top:37px;width:260px">Full room makeovers from plan to final coat of paint. We update floors, walls, lighting and fixtures so older homes feel fresh, safe and comfortable again without stress or surprise costs.</p>
    <svg class="hex-icon" style="left:706px;top:8px" viewBox="0 0 82 90"><polygon points="41,4 77,24 77,66 41,86 5,66 5,24" fill="#fff" stroke="var(--red)" stroke-width="5"/><path d="M41 34l12 10v12H29V44z" fill="var(--icon)"/><path d="M22 42a19 19 0 0 1 32-12M60 48a19 19 0 0 1-32 12" fill="none" stroke="var(--icon)" stroke-width="2.5"/></svg>
    <div class="divider" style="left:397px;top:104px;width:397px"></div>

    <div class="service-label" style="left:397px;top:116px"><b style="width:126px">REMODEL</b><i></i></div>
    <p class="service-copy" style="left:418px;top:138px;width:260px">Kitchen and bathroom remodels with grab bars, walk-in showers and easy-reach storage for seniors. We manage every trade so your project stays on budget and on schedule.</p>
    <svg class="hex-icon" style="left:706px;top:108px" viewBox="0 0 82 90"><polygon points="41,4 77,24 77,66 41,86 5,66 5,24" fill="#fff" stroke="var(--red)" stroke-width="5"/><path d="M41 24L20 42h5v22h32V42h5z" fill="var(--icon)"/><circle cx="41" cy="50" r="7" fill="#fff"/></svg>
    <div class="divider" style="left:397px;top:205px;width:397px"></div>

    <div class="service-label" style="left:397px;top:214px"><b style="width:126px">CLEANING SERVICES</b><i></i></div>
    <p class="service-copy" style="left:418px;top:236px;width:260px">Move-in, move-out and post-construction cleaning for homes and rentals. Dust, debris and stains removed so your space is ready to enjoy or show to new tenants right away.</p>
    <svg class="hex-icon" style="left:706px;top:211px" viewBox="0 0 82 90"><polygon points="41,4 77,24 77,66 41,86 5,66 5,24" fill="#fff" stroke="var(--red)" stroke-width="5"/><path d="M30 24l6 28" stroke="var(--icon)" stroke-width="3"/><path d="M31 52h12l4 10H27z" fill="var(--icon)"/><path d="M49 50h12l-2 14h-8z" fill="var(--icon)"/></svg>
    <div class="divider" style="left:397px;top:306px;width:397px"></div>

    <div class="service-label" style="left:397px;top:313px"><b style="width:126px">LANDSCAPING</b><i></i></div>
    <p class="service-copy" style="left:418px;top:334px;width:260px">Lawn care, planting, mulching, edging and seasonal cleanup. We build paths, small walls and garden beds that raise curb appeal and are easy to keep neat all year long.</p>
    <svg class="hex-icon" style="left:706px;top:316px" viewBox="0 0 82 90"><polygon points="41,4 77,24 77,66 41,86 5,66 5,24" fill="#fff" stroke="var(--red)" stroke-width="5"/><path d="M32 26l12 24" stroke="var(--icon)" stroke-width="4"/><path d="M40 48l10-4 4 10-10 4z" fill="var(--icon)"/><path d="M22 66q19-10 38 0z" fill="var(--icon)"/></svg>
  </div>

  <div class="rental">
    <h3>RENTAL MAINTENANCE.</h3>
    <ul>
      <li><svg viewBox="0 0 8 8"><circle cx="4" cy="4" r="3.5" fill="none" stroke="var(--red)"/><path d="M2.2 4.1l1.3 1.3 2.4-2.7" fill="none" stroke="var(--red)"/></svg>Turnover repairs between tenants, done fast.</li>
      <li><svg viewBox="0 0 8 8"><circle cx="4" cy="4" r="3.5" fill="none" stroke="var(--red)"/><path d="M2.2 4.1l1.3 1.3 2.4-2.7" fill="none" stroke="var(--red)"/></svg>Painting, patching and fixture replacement.</li>
      <li><svg viewBox="0 0 8 8"><circle cx="4" cy="4" r="3.5" fill="none" stroke="var(--red)"/><path d="M2.2 4.1l1.3 1.3 2.4-2.7" fill="none" stroke="var(--red)"/></svg>Scheduled inspections for plumbing, electrical and safety devices, with a clear report after every visit.</li>
      <li><svg viewBox="0 0 8 8"><circle cx="4" cy="4" r="3.5" fill="none" stroke="var(--red)"/><path d="M2.2 4.1l1.3 1.3 2.4-2.7" fill="none" stroke="var(--red)"/></svg>Quick response to tenant calls and urgent repairs, so landlords and property managers can relax.</li>
      <li><svg viewBox="0 0 8 8"><circle cx="4" cy="4" r="3.5" fill="none" stroke="var(--red)"/><path d="M2.2 4.1l1.3 1.3 2.4-2.7" fill="none" stroke="var(--red)"/></svg>Seasonal yard and exterior upkeep.</li>
    </ul>
  </div>
</section>

</body>
</html>
```